Cobalt Reclaim Partners is a recycling company. We have started a marketing campaign and would love your artwork to help us get started. We would like the fallowing to be on our postcard:
At the top please write: Now servicing businesses in the city of Industry!
Below that we would like 3 pictures.. The first is a picture of trash, the second is a our logo and at plus sign. After that would be a picture of neat baled recycled material and the last picture would be money. Below this please right the following:
- Companies choose cobalt reclaim partners because:
- if it can be recycled we will find a use for it
- we pay top dollar
- starting our service is fast and easy
* All it takes is one call/email and we will handle the rest
At the bottom please put our contact information
- 800.514.2276
- maribel@salvorix27.com
- salvorix27.com

Thanks guys! I have attached our logo!

I am sorry for this late post,but could you not put anything on the back except for a return address which is 1847 Dorrance Ave Costa Mesa, Ca 92926 Thank you! We have had a lot of trouble in the past with the post office when we put stuff on the back for some reason.

```html
<!DOCTYPE html>
<html lang="en">
<head>
<meta charset="utf-8">
<title>Cobalt Reclaim Partners – Postcard Back</title>
<link rel="stylesheet" href="https://fonts.googleapis.com/css2?family=Arimo:wght@400;700&display=swap">
<style>
  :root {
    --paper: #ffffff;
    --edge-shade: #dcdad8;
    --ink: #1d1d1b;
    --brand-green: #5fa544;
    --rule: #d9d9d9;
    --stamp-border: #d6d6d6;
  }
  html, body {
    margin: 0;
    padding: 0;
    width: 1200px;
    height: 777px;
    overflow: hidden;
    background: var(--paper);
  }
  .postcard-back {
    position: relative;
    width: 1200px;
    height: 777px;
    overflow: hidden;
    font-family: "Arimo", Arial, sans-serif;
    color: var(--ink);
    background:
      linear-gradient(90deg, var(--edge-shade) 0px, rgba(236,234,232,0.7) 40px, rgba(255,255,255,0) 140px),
      radial-gradient(ellipse 900px 160px at 420px 0px, rgba(232,230,228,0.9), rgba(255,255,255,0) 100%),
      var(--paper);
  }
  .brand-name {
    position: absolute;
    left: 20px;
    top: 124px;
    display: flex;
    align-items: center;
    gap: 11px;
    margin: 0;
    font-size: 31px;
    font-weight: 700;
    color: var(--ink);
    letter-spacing: -0.3px;
    white-space: nowrap;
  }
  .brand-mark {
    width: 21px;
    height: 21px;
    background: var(--brand-green);
    flex: none;
  }
  .return-tab {
    position: absolute;
    left: 418px;
    top: 0;
    width: 41px;
    height: 105px;
    background: var(--brand-green);
    border-radius: 0 0 20px 20px;
  }
  .return-tab svg {
    position: absolute;
    left: 10px;
    top: 37px;
    width: 21px;
    height: 21px;
  }
  .return-address {
    position: absolute;
    left: 465px;
    top: 31px;
    margin: 0;
    font-style: normal;
    font-size: 27px;
    line-height: 33px;
    color: var(--ink);
    white-space: nowrap;
  }
  .stamp-box {
    position: absolute;
    left: 1005px;
    top: 18px;
    width: 171px;
    height: 170px;
    border: 1.5px solid var(--stamp-border);
    box-sizing: border-box;
    background: var(--paper);
  }
  .recipient-lines {
    position: absolute;
    left: 834px;
    top: 411px;
    width: 322px;
  }
  .recipient-lines span {
    display: block;
    height: 0;
    border-top: 2px solid var(--rule);
    margin-bottom: 53px;
  }
</style>
</head>
<body>
  <main class="postcard-back">
    <h1 class="brand-name"><span class="brand-mark"></span>cobalt reclaim partners</h1>

    <div class="return-tab">
      <svg viewBox="0 0 20 20" aria-hidden="true">
        <path d="M10 2 L19 10 H16 V18 H12 V13 H8 V18 H4 V10 H1 Z" fill="#ffffff"/>
      </svg>
    </div>
    <address class="return-address">1847 Dorrance Ave<br>Lindell Park ca 92847</address>

    <div class="stamp-box"></div>

    <div class="recipient-lines">
      <span></span><span></span><span></span><span></span>
    </div>
  </main>
</body>
</html>
```